Business Card Professional Clean - Ledgerpeak

Create a business card for my company that deals with Cryptocurrencies. I have a few designs ideas that I'd like to be implemented. Thanks! I will include the logo files, and a link to the design styles that I like.

Target Market(s)

Professionals

Industry/Entity Type

Consulting

Contact Information for Business Card

Name: Mark Dunn
Title: CEO/Technical Director
Phone: (587)430-9158
E-mail: mdunn@ledgerpeak.example
Address: Suite 512, 208-3375 Harwood Lane NW

Twitter: @LedgerPeakYYC
Instagram: ledgerpeakyyc

Colors
92b5d7
3276b5
33a6d7
85acd3
85cae6
0592cd

Requirements
Must have
• Some colors that match with the logo and the pictures I put in below.
• Ideally the finished product would look something like the attachments showing the color gradient I want.
Nice to have
• Please see some of the attachments I've included. This is very close to the final product that I would like to see. If someone could recreate something like those I would definitely feel pretty good about it.
• For the instagram and twitter please use the symbols/icon to represent it on the card.
Should not have
• No crazy colors and unprofessional styles. I just want clear info. Don't go outside the boundaries of the colors in the attachment and we should be good. No crazy weird fonts either.

```html
<!DOCTYPE html>
<html lang="en">
<head>
<meta charset="utf-8">
<title>Ledgerpeak Business Card</title>
<link rel="stylesheet" href="https://fonts.googleapis.com/css2?family=Cinzel:wght@500&family=Montserrat:wght@700&family=Lato:wght@400&display=swap">
<style>
  :root {
    --backdrop: #d9dde2;
    --navy: #0f1a26;
    --navy-deep: #0a121b;
    --paper: #f4f5f6;
    --brand-blue: #2f6cc0;
    --band-blue: #3276b5;
    --band-light: #3a86d0;
    --band-shade: #25599a;
    --slate: #5f6b78;
    --text-light: #e9eef4;
    --text-soft: #c9d6e4;
  }
  * { margin: 0; padding: 0; box-sizing: border-box; }
  html, body { width: 1200px; height: 900px; overflow: hidden; }
  body { background: var(--backdrop); position: relative; font-family: "Lato", sans-serif; }

  .card { position: absolute; border-radius: 22px; overflow: hidden; box-shadow: 0 10px 30px rgba(0,0,0,.18); }

  /* Front card (portrait) */
  .card-front { left: 130px; top: 150px; width: 340px; height: 600px; background: var(--paper); }
  .front-dark {
    position: absolute; left: 0; top: 250px; width: 100%; height: 350px;
    background: radial-gradient(circle at 60% 40%, #15222f 0%, var(--navy) 55%, var(--navy-deep) 100%);
  }
  .front-wordmark {
    position: absolute; left: 0; top: 150px; width: 100%; text-align: center;
    font-family: "Cinzel", serif; font-weight: 500; font-size: 34px; color: var(--brand-blue);
    letter-spacing: 1px;
  }
  .front-band { position: absolute; left: 0; top: 222px; width: 340px; height: 110px; }
  .holder { position: absolute; left: 0; top: 244px; width: 100%; text-align: center; color: #fff; }
  .holder-name { font-family: "Montserrat", sans-serif; font-weight: 700; font-size: 27px; letter-spacing: .5px; }
  .holder-title { font-size: 15px; margin-top: 2px; color: var(--text-light); }

  .contact-list { position: absolute; left: 54px; top: 372px; list-style: none; }
  .contact-list li { display: flex; align-items: center; height: 34px; color: var(--text-light); font-size: 17px; }
  .contact-list li.address { align-items: flex-start; height: auto; padding-top: 6px; line-height: 1.35; }
  .contact-icon { width: 18px; height: 18px; margin-right: 16px; flex: none; fill: var(--band-light); }
  .contact-list li.address .contact-icon { margin-top: 2px; }

  /* Back card (landscape) */
  .card-back {
    left: 560px; top: 290px; width: 560px; height: 320px;
    background: radial-gradient(circle at 65% 45%, #162433 0%, var(--navy) 55%, var(--navy-deep) 100%);
  }
  .back-band { position: absolute; left: 120px; top: 0; width: 90px; height: 320px; }
  .back-url {
    position: absolute; left: 165px; top: 160px; transform: translate(-50%, -50%) rotate(90deg);
    white-space: nowrap; font-family: "Cinzel", serif; font-weight: 500; font-size: 13px;
    letter-spacing: 3px; color: var(--text-soft);
  }
  .back-logo { position: absolute; left: 240px; top: 130px; width: 300px; display: flex; align-items: center; gap: 14px; justify-content: center; }
  .back-mark { width: 30px; height: 30px; border: 3px solid var(--slate); flex: none; }
  .back-wordmark { font-family: "Cinzel", serif; font-weight: 500; font-size: 38px; color: var(--brand-blue); letter-spacing: 1px; }
</style>
</head>
<body>

<section class="card card-front" aria-label="Business card front">
  <div class="front-dark" role="img" aria-label="Dark navy background with a faint world map texture"></div>
  <div class="front-wordmark">Ledgerpeak</div>
  <svg class="front-band" viewBox="0 0 340 110" aria-hidden="true">
    <polygon points="0,28 60,28 78,8 262,8 280,28 340,28 340,96 280,96 262,108 78,108 60,96 0,96" fill="var(--band-blue)"/>
    <polygon points="0,28 60,28 60,96 0,96" fill="var(--band-shade)"/>
    <polygon points="280,28 340,28 340,96 280,96" fill="var(--band-shade)"/>
    <polygon points="60,28 78,8 78,108 60,96" fill="var(--band-light)"/>
    <polygon points="280,28 262,8 262,108 280,96" fill="var(--band-light)"/>
  </svg>
  <div class="holder">
    <div class="holder-name">MARK DUNN</div>
    <div class="holder-title">CEO/Technical Director</div>
  </div>
  <ul class="contact-list">
    <li>
      <svg class="contact-icon" viewBox="0 0 24 24"><path d="M6.6 10.8a15.1 15.1 0 0 0 6.6 6.6l2.2-2.2c.3-.3.7-.4 1-.2 1.1.4 2.3.6 3.6.6.6 0 1 .4 1 1V20c0 .6-.4 1-1 1A17 17 0 0 1 3 4c0-.6.4-1 1-1h3.5c.6 0 1 .4 1 1 0 1.3.2 2.5.6 3.6.1.3 0 .7-.2 1z"/></svg>
      (587)430-9158
    </li>
    <li>
      <svg class="contact-icon" viewBox="0 0 24 24"><path d="M2 5h20v14H2z M3.5 6.5 12 13l8.5-6.5" fill="none" stroke="var(--band-light)" stroke-width="2"/></svg>
      mdunn@ledgerpeak.example
    </li>
    <li>
      <svg class="contact-icon" viewBox="0 0 24 24"><circle cx="12" cy="12" r="9"/></svg>
      @LedgerPeakYYC
    </li>
    <li>
      <svg class="contact-icon" viewBox="0 0 24 24"><rect x="3" y="3" width="18" height="18" rx="4"/></svg>
      ledgerpeakyyc
    </li>
    <li class="address">
      <svg class="contact-icon" viewBox="0 0 24 24"><path d="M12 2a7 7 0 0 0-7 7c0 5 7 13 7 13s7-8 7-13a7 7 0 0 0-7-7zm0 9.5A2.5 2.5 0 1 1 12 6.5a2.5 2.5 0 0 1 0 5z"/></svg>
      <span>Suite 512, 208-3375<br>Harwood Lane NW</span>
    </li>
  </ul>
</section>

<section class="card card-back" role="img" aria-label="Business card back: dark navy with a faint world map texture">
  <svg class="back-band" viewBox="0 0 90 320" aria-hidden="true">
    <polygon points="10,0 80,0 80,50 72,68 72,252 80,270 80,320 10,320 10,270 18,252 18,68 10,50" fill="var(--band-blue)"/>
    <polygon points="10,0 80,0 80,50 10,50" fill="var(--band-shade)"/>
    <polygon points="10,270 80,270 80,320 10,320" fill="var(--band-shade)"/>
    <polygon points="10,50 80,50 72,68 18,68" fill="var(--band-light)"/>
    <polygon points="18,252 72,252 80,270 10,270" fill="var(--band-light)"/>
  </svg>
  <div class="back-url">WWW.LEDGERPEAK.EXAMPLE</div>
  <div class="back-logo">
    <div class="back-mark"></div>
    <div class="back-wordmark">Ledgerpeak</div>
  </div>
</section>

</body>
</html>
```